A business selling natural soaps online and in farmers markets. I want it to reflect local commerce and natural lifestyle. My colors are olive green and saddle brown. I want the dimensions to be 2.25 x 3.25" with matte finish.

The name of my company is Fernwick Soapery, LLC

Business

```html
<!DOCTYPE html>
<html lang="en">
<head>
<meta charset="utf-8">
<title>Fernwick Soapery, LLC — Business Card</title>
<link rel="stylesheet" href="https://fonts.googleapis.com/css2?family=Arimo&family=Cabin:wght@600&family=Open+Sans&family=Tinos:wght@700&display=swap">
<style>
  :root {
    --leaf-light: #a6ca84;
    --leaf-mid: #93bd6c;
    --leaf-deep: #7eac55;
    --ink: #111111;
    --bark: #6f6757;
    --mark-tone: #7b6e60;
  }
  html, body {
    margin: 0;
    padding: 0;
    overflow: hidden;
    background: #ffffff;
  }
  .card {
    position: relative;
    width: 1200px;
    height: 839px;
    overflow: hidden;
    background: var(--leaf-light);
  }
  .card__texture {
    position: absolute;
    inset: 0;
    background:
      radial-gradient(ellipse 520px 420px at 62% 42%, var(--leaf-deep) 0%, rgba(126,172,85,0) 70%),
      linear-gradient(90deg, var(--leaf-light) 0%, var(--leaf-mid) 55%, var(--leaf-light) 100%);
  }
  .card__mark {
    position: absolute;
    left: 56px;
    top: 150px;
    width: 330px;
    height: 330px;
    background: var(--mark-tone);
  }
  .card__web {
    position: absolute;
    left: 408px;
    top: 178px;
    margin: 0;
    font-family: "Open Sans", sans-serif;
    font-weight: 400;
    font-size: 90px;
    line-height: 1;
    color: var(--ink);
    letter-spacing: -1px;
  }
  .card__owner {
    position: absolute;
    left: 560px;
    width: 470px;
    top: 352px;
    margin: 0;
    text-align: center;
    font-family: "Arimo", sans-serif;
    font-size: 46px;
    line-height: 1;
    color: var(--ink);
  }
  .card__email {
    position: absolute;
    right: 49px;
    top: 565px;
    margin: 0;
    font-family: "Tinos", serif;
    font-weight: 700;
    font-size: 46px;
    line-height: 1;
    color: var(--ink);
  }
  .card__rule {
    position: absolute;
    left: 62px;
    top: 630px;
    width: 1089px;
    height: 5px;
    background: var(--ink);
  }
  .card__company {
    position: absolute;
    left: 62px;
    width: 1089px;
    top: 648px;
    margin: 0;
    text-align: center;
    font-family: "Cabin", sans-serif;
    font-weight: 600;
    font-size: 100px;
    line-height: 1;
    letter-spacing: 2px;
    color: var(--bark);
  }
</style>
</head>
<body>
  <main class="card">
    <div class="card__texture" role="img" aria-label="Painted green brush-stroke texture"></div>
    <div class="card__mark" aria-hidden="true"></div>
    <p class="card__web">fernwicksoap.com</p>
    <p class="card__owner">Clara Whitfield, Owner</p>
    <p class="card__email">info@fernwicksoap.com</p>
    <div class="card__rule"></div>
    <h1 class="card__company">Fernwick Soapery, LLC</h1>
  </main>
</body>
</html>
```